menu board design: harbor burger

we are a burger restaurant.
we need to re design our menu board to fit within the new design of the restaurant. we are after something simple and easy to read. the overall look and feel of the design should be inline with the design of the shop.

Target Market(s)

18-40 male and female

Colors

Designer to choose colors to be used in the design.

Requirements
Must have
• easy to read. good layout. white background. branding included in design.

```html
<!DOCTYPE html>
<html lang="en">
<head>
<meta charset="utf-8">
<title>Harbor Burger Menu Board</title>
<link href="https://fonts.googleapis.com/css2?family=Bebas+Neue&family=Montserrat:wght@400;500;600;700&display=swap" rel="stylesheet">
<style>
  :root {
    --blue: #1f56a7;
    --ink: #111111;
    --board: #ffffff;
    --wash: #efefef;
    --surround: #000000;
  }
  * { box-sizing: border-box; margin: 0; padding: 0; }
  html, body { width: 1200px; height: 532px; overflow: hidden; background: var(--surround); }
  .canvas { position: relative; width: 1200px; height: 532px; background: var(--surround); font-family: "Montserrat", sans-serif; }
  .board { position: absolute; left: 29px; top: 28px; width: 1142px; height: 476px; background: var(--board); }
  .frame { position: absolute; left: 39px; top: 38px; width: 1121px; height: 455px; border: 5px solid var(--blue); border-radius: 12px; background: var(--wash); }
  .frame::after { content: ""; position: absolute; inset: 1px; border: 1.5px solid var(--blue); border-radius: 7px; }

  .section-head { position: absolute; top: 55px; display: flex; align-items: flex-start; }
  .section-title { font-family: "Bebas Neue", sans-serif; font-size: 40px; line-height: 34px; color: var(--blue); letter-spacing: -2.5px; }
  .section-bar { width: 2.5px; height: 27px; background: var(--ink); margin: 3px 7px 0 8px; }
  .section-note { font-size: 6.2px; line-height: 7.3px; color: var(--ink); margin-top: 4px; }
  .section-note.spaced { letter-spacing: 0.6px; }

  .item { position: absolute; }
  .item-line { display: flex; align-items: flex-end; height: 20px; color: var(--blue); font-size: 15.5px; font-weight: 500; line-height: 20px; white-space: nowrap; }
  .item-line.small { font-size: 12px; }
  .leader { flex: 1; height: 2px; margin: 0 1px 5px; background: radial-gradient(circle, var(--blue) 0.8px, transparent 1px) 0 0 / 3.5px 2px repeat-x; }
  .item-desc { margin-top: 1px; padding-left: 2px; font-size: 7.1px; line-height: 8px; color: var(--ink); white-space: nowrap; }
  .item-desc.caps { text-transform: uppercase; font-weight: 500; font-size: 6.8px; }
  .item-desc .count { color: var(--blue); }

  .beef, .sides { left: 61px; width: 340px; }
  .chicken { left: 441px; width: 320px; }
  .fries { left: 801px; width: 338px; }
  .packs { left: 801px; width: 207px; }

  .divider { position: absolute; top: 106px; height: 175px; border-left: 1.5px dashed var(--ink); }

  .sides-title { position: absolute; left: 157px; top: 314px; width: 150px; display: flex; align-items: center; justify-content: center; gap: 6px; }
  .sides-title .ribbon { width: 40px; height: 26px; background: var(--blue); }
  .sides-title span { font-family: "Bebas Neue", sans-serif; font-size: 34px; line-height: 30px; color: var(--blue); letter-spacing: -1.5px; }

  .ribs-head { position: absolute; left: 801px; top: 372px; display: flex; align-items: center; }
  .ribs-head .name { font-size: 15.5px; font-weight: 500; color: var(--blue); line-height: 20px; }
  .ribs-head .section-bar { height: 18px; margin: 0 5px 0 5px; width: 1.5px; }
  .ribs-head .section-note { margin-top: 0; font-size: 6.6px; line-height: 8.4px; font-weight: 500; }
  .sauce-choice { position: absolute; left: 801px; top: 395px; font-size: 10px; font-weight: 700; color: var(--blue); white-space: nowrap; }
  .sauce-choice .or { color: var(--ink); font-weight: 500; margin: 0 4px; }

  .brand { position: absolute; left: 1018px; top: 405px; width: 132px; text-align: center; color: var(--blue); }
  .brand-name { font-size: 18px; font-weight: 700; line-height: 22px; }
  .brand-tag { margin-top: 36px; font-size: 4.8px; letter-spacing: 1.6px; }
</style>
</head>
<body>
<div class="canvas">
  <div class="board"></div>
  <div class="frame"></div>

  <div class="section-head" style="left:60px">
    <h2 class="section-title">Beef Burgers</h2>
    <div class="section-bar"></div>
    <p class="section-note">100% natural beef without any additives or perservatives.<br><span style="letter-spacing:0.5px">We know because we grind it ourselves! Smashed</span><br>to order on a hot grill rite in front of you.</p>
  </div>
  <div class="item beef" style="top:95px"><div class="item-line">CHEESEBURGER<i class="leader"></i>9.5</div><p class="item-desc">Dill Pickles, minced onion, American cheddar, mustard and ketchup.</p></div>
  <div class="item beef" style="top:129px"><div class="item-line">Flame Grill<i class="leader"></i>9.5</div><p class="item-desc">Shredded lettuce, sliced tomato, minced onion, dill pickles,american chedar, mayo and ketchup.</p></div>
  <div class="item beef" style="top:164px"><div class="item-line">Big Mic<i class="leader"></i>9.9</div><p class="item-desc">Shredded lettuce, dill pickles, minced onion, American cheddar and special sauce.</p></div>
  <div class="item beef" style="top:199px"><div class="item-line">Truffled<i class="leader"></i>9.9</div><p class="item-desc">Fresh Rocket, caramelised onion, dill pickles, havarti cheese and truffle infused mayo</p></div>
  <div class="item beef" style="top:233px"><div class="item-line">CHEESE DELUXE<i class="leader"></i>9.5</div><p class="item-desc">Caramelised onion, american chedar, dill pickles and special sauce.</p></div>
  <div class="item beef" style="top:268px"><div class="item-line">CALI BURGER<i class="leader"></i>9.9</div><p class="item-desc">Iceburg lettuce, sliced tomato, American chedar, minced onion, crinkle cut pickleS, pink sauce.</p></div>

  <div class="divider" style="left:420px"></div>
  <div class="divider" style="left:780px"></div>

  <div class="section-head" style="left:441px">
    <h2 class="section-title">Chicken Burgers</h2>
    <div class="section-bar"></div>
    <p class="section-note spaced">famous southern style fried<br>chicken with secret seasoning</p>
  </div>
  <div class="item chicken" style="top:95px"><div class="item-line">ORIGINAL<i class="leader"></i>8.9</div><p class="item-desc">Shredded lettuce and mayo.</p></div>
  <div class="item chicken" style="top:129px"><div class="item-line">HOT N SPICY<i class="leader"></i>9.5</div><p class="item-desc">Shredded lettuce, mayo and pirri pirri.</p></div>
  <div class="item chicken" style="top:164px"><div class="item-line">KENTUCKY<i class="leader"></i>9.9</div><p class="item-desc">Shredded lettuce, swiss cheese and feisty mayo.</p></div>
  <div class="item chicken" style="top:199px"><div class="item-line">BUFFALO BILL<i class="leader"></i>9.9</div><p class="item-desc">smothered in hot sauce, creamy slaw, american chedar and ranch.</p></div>
  <div class="item chicken" style="top:233px"><div class="item-line">SOUTHERN FRIED CHICKEN<i class="leader"></i>9.9</div><p class="item-desc">Creamy slaw, crinkle cut pickles, american chedar and chipotle mayo.</p></div>
  <div class="item chicken" style="top:268px"><div class="item-line">SMOKY BBQ<i class="leader"></i>9.9</div><p class="item-desc">smothered in smoky bbq, creamy slaw, american chedar and ranch.</p></div>

  <div class="section-head" style="left:801px">
    <h2 class="section-title">Loaded Fries</h2>
    <div class="section-bar"></div>
    <p class="section-note spaced">A SELECTION OF CLASSIC LOADED<br>FRIES COMBINATIONS.</p>
  </div>
  <div class="item fries" style="top:95px"><div class="item-line">CHEESY FRIES<i class="leader"></i>5.5</div><p class="item-desc caps">with chedar cheese sauce</p></div>
  <div class="item fries" style="top:129px"><div class="item-line">CREAMY MUSHROOM FRIES<i class="leader"></i>6.9</div><p class="item-desc caps">with classic creamy mushroom sauce</p></div>
  <div class="item fries" style="top:164px"><div class="item-line">CLASSIC GRAVY FRIES<i class="leader"></i>5.5</div><p class="item-desc caps">with chedar cheese sauce</p></div>
  <div class="item fries" style="top:199px"><div class="item-line">PARMESAN&nbsp; TRUFFLE<i class="leader"></i>6.9</div><p class="item-desc caps">with truffle infused mayo and parmesan cheese</p></div>
  <div class="item fries" style="top:233px"><div class="item-line">BEEF CHILLI FRIES<i class="leader"></i>9.9</div><p class="item-desc caps">with salsa, jalapeno, sour cream, cheese sauce and beef chilli</p></div>
  <div class="item fries" style="top:268px"><div class="item-line">GUACAMOLE FRIES<i class="leader"></i>9.9</div><p class="item-desc caps">with salsa, jalapeno, sour cream, cheese sauce and guacamole.</p></div>
  <div class="item fries" style="top:303px"><div class="item-line">MACHOS FRIES<i class="leader"></i>11.5</div><p class="item-desc caps">with beef and guacamole.</p></div>

  <div class="sides-title">
    <div class="ribbon" role="img" aria-label="Ribbon banner ornament"></div>
    <span>SIDES</span>
    <div class="ribbon" role="img" aria-label="Ribbon banner ornament"></div>
  </div>
  <div class="item sides" style="top:348px"><div class="item-line">Fries<i class="leader"></i>3.5</div></div>
  <div class="item sides" style="top:373px"><div class="item-line">Kentucky Tenders<i class="leader"></i>6.9</div><p class="item-desc">Breaded and fried chicken with secret seasoning <span class="count">(2 pcs)</span></p></div>
  <div class="item sides" style="top:410px"><div class="item-line">ONION RINGS<i class="leader"></i>5.0</div><p class="item-desc caps">battered and fried onion rings</p></div>
  <div class="item sides" style="top:447px"><div class="item-line">GUACAMOLE NACHOS<i class="leader"></i>11.5</div><p class="item-desc caps" style="font-size:6.6px">freshly cooked corn chips, salsa, jalapeno, sour cream, cheese sauce and guacamole.</p></div>

  <div class="item chicken" style="top:372px"><div class="item-line">BEEF CHILLI NACHOS<i class="leader"></i>11.5</div><p class="item-desc caps" style="font-size:6.4px">freshly cooked corn chips, salsa, jalapeno, sour cream, cheese sauce and beef chilli</p></div>
  <div class="item chicken" style="top:410px"><div class="item-line">MACHOS NACHOS<i class="leader"></i>13.5</div><p class="item-desc caps">beef and guacamole nachos.</p></div>
  <div class="item chicken" style="top:447px"><div class="item-line">COLESLAW<i class="leader"></i>5.0</div><p class="item-desc caps">classic creamy slaw</p></div>

  <div class="ribs-head">
    <span class="name">BUFALLO RIBS</span>
    <div class="section-bar"></div>
    <p class="section-note">BUFALLO STYLE CHICKEN RIBS<br>SMOTHERED IN EITHER</p>
  </div>
  <p class="sauce-choice">CLASSIC HOT SAUCE<span class="or">OR</span>SMOKY BBQ.</p>
  <div class="item packs" style="top:408px"><div class="item-line small">6 PACK<i class="leader"></i>6.9</div></div>
  <div class="item packs" style="top:428px"><div class="item-line small">12 PACK<i class="leader"></i>12.9</div></div>
  <div class="item packs" style="top:448px"><div class="item-line small">24 PACK<i class="leader"></i>23.9</div></div>

  <div class="brand">
    <p class="brand-name">harbor burger</p>
    <p class="brand-tag">FRESH OFF THE GRILL</p>
  </div>
</div>
</body>
</html>
```